Design Bramwell Precast Core Values

We are a precast concrete manufacturing company that is looking to present (and eventually include in marketing) our core values to our employees (and eventually our customers). These values represent the morals, motivation and mission of our company. It is important to use these statements for evaluating performance and communicating who we are to both potential new-hires as well as new contractors.
Please design a graphic, hopefully using a product (or similar storm drain picture) image to organize the following:
BRAMWELL PRECAST CORE VALUES
1. We are committed to one another
• Coaching culture
• LMA (lead, manage, accountability)
• Employees win
• Zero 4 Ever
2. We know what our customers need
• Extensive experience
• Value engineering
• Excellent communication
3. We go the extra “yard”
• Follow up, follow through
• “Can do” attitude
• Do the little things well (Do the ordinary extraordinarily)

```html
<!DOCTYPE html>
<html lang="en">
<head>
<meta charset="utf-8">
<title>Bramwell Precast Core Values</title>
<link rel="stylesheet" href="https://fonts.googleapis.com/css2?family=Nunito:wght@900&family=Roboto+Condensed:wght@400;700&display=swap">
<style>
  :root {
    --sky: #1ff2f4;
    --sky-deep: #12d9e4;
    --band-blue: #0a0ae6;
    --band-edge: #5a8cff;
    --white: #ffffff;
    --icon-fill: rgba(255,255,255,.35);
    --ink: #111111;
    --navy: #26306a;
    --gold-top: #fff200;
    --gold-mid: #ffd400;
    --gold-bottom: #f58a00;
    --brand-gold: #f5e11a;
  }
  * { box-sizing: border-box; margin: 0; padding: 0; }
  html, body { width: 1200px; height: 848px; overflow: hidden; background: var(--sky); }
  .stage {
    position: relative;
    width: 1200px;
    height: 848px;
    overflow: hidden;
    background: var(--sky);
    font-family: "Roboto Condensed", "Arial Narrow", sans-serif;
  }
  .backdrop {
    position: absolute; inset: 0;
    background: radial-gradient(ellipse at 30% 55%, var(--sky-deep) 0%, rgba(18,217,228,0) 55%),
                radial-gradient(ellipse at 80% 50%, var(--sky-deep) 0%, rgba(18,217,228,0) 50%);
    opacity: .6;
  }
  .brand {
    position: absolute; top: 72px; left: 0; width: 1200px;
    display: flex; justify-content: center; align-items: center; gap: 12px;
  }
  .brand-dot { width: 46px; height: 46px; border-radius: 50%; background: var(--brand-gold); }
  .brand-name { font-weight: 700; font-size: 27px; color: var(--ink); letter-spacing: .2px; }
  .title-band {
    position: absolute; top: 137px; left: 0; width: 1200px; height: 77px;
    background: var(--band-blue);
    border-top: 3px solid var(--band-edge);
    border-bottom: 3px solid var(--band-edge);
    display: flex; align-items: center; justify-content: center;
  }
  .title {
    font-family: "Nunito", "Arial Rounded MT Bold", sans-serif;
    font-weight: 900; font-size: 58px; color: var(--white); letter-spacing: 1px;
    text-shadow: 0 0 6px #9fc4ff, 0 0 12px #6e9cff;
  }
  .divider { position: absolute; top: 268px; width: 2px; height: 555px; background: var(--white); }
  .divider.one { left: 381px; }
  .divider.two { left: 754px; }
  .icon { position: absolute; top: 279px; width: 176px; height: 176px; }
  .icon.commit { left: 80px; }
  .icon.listen { left: 473px; }
  .icon.measure { left: 857px; }
  .value-band {
    position: absolute; top: 481px; left: 0; width: 1200px; height: 134px;
    background: linear-gradient(to bottom, var(--gold-top) 0%, var(--gold-mid) 45%, var(--gold-bottom) 100%);
  }
  .value-title {
    position: absolute; top: 0; height: 134px;
    display: flex; align-items: center; justify-content: center; text-align: center;
    font-family: "Nunito", "Arial Rounded MT Bold", sans-serif;
    font-weight: 900; font-size: 28px; line-height: 1.22; color: var(--ink); text-transform: uppercase;
  }
  .value-title.commit { left: 40px; width: 260px; }
  .value-title.listen { left: 400px; width: 330px; }
  .value-title.measure { left: 800px; width: 364px; }
  .points {
    position: absolute; top: 640px; list-style: none;
    font-size: 26px; line-height: 42px; color: var(--navy);
  }
  .points li { position: relative; padding-left: 20px; }
  .points li::before { content: "•"; position: absolute; left: 0; }
  .points .sub { display: block; line-height: 32px; }
  .points.commit { left: 44px; width: 320px; }
  .points.commit li:first-child { line-height: 34px; padding-top: 4px; padding-bottom: 4px; }
  .points.listen { left: 410px; width: 330px; }
  .points.measure { left: 786px; width: 400px; }
</style>
</head>
<body>
<main class="stage">
  <div class="backdrop" role="img" aria-label="Faint line drawings of precast storm drain structures and grates"></div>

  <header class="brand">
    <span class="brand-dot"></span>
    <span class="brand-name">Bramwell Precast</span>
  </header>

  <div class="title-band"><h1 class="title">CORE VALUES</h1></div>

  <span class="divider one"></span>
  <span class="divider two"></span>

  <svg class="icon commit" viewBox="0 0 176 176" role="img" aria-label="Handshake icon">
    <circle cx="88" cy="88" r="80" fill="none" stroke="#fff" stroke-width="9"/>
    <circle cx="88" cy="88" r="60" fill="var(--icon-fill)"/>
  </svg>
  <svg class="icon listen" viewBox="0 0 176 176" role="img" aria-label="Ear icon">
    <circle cx="88" cy="88" r="80" fill="none" stroke="#fff" stroke-width="9"/>
    <circle cx="88" cy="88" r="60" fill="var(--icon-fill)"/>
  </svg>
  <svg class="icon measure" viewBox="0 0 176 176" role="img" aria-label="Measuring ruler icon">
    <circle cx="88" cy="88" r="80" fill="none" stroke="#fff" stroke-width="9"/>
    <circle cx="88" cy="88" r="60" fill="var(--icon-fill)"/>
  </svg>

  <section class="value-band">
    <h2 class="value-title commit">Coaching<br>Culture</h2>
    <h2 class="value-title listen">We know what<br>our customers<br>need</h2>
    <h2 class="value-title measure">We go the<br>extra “yard”</h2>
  </section>

  <ul class="points commit">
    <li>LMA (lead, manage, accountability)</li>
    <li>Employees win</li>
    <li>Zero 4 Ever</li>
  </ul>
  <ul class="points listen">
    <li>Extensive experience</li>
    <li>Value engineering</li>
    <li>Excellent communication</li>
  </ul>
  <ul class="points measure">
    <li>Follow up, follow through</li>
    <li>“Can do” attitude</li>
    <li>Do the little things well<span class="sub">(Do the ordinary extraordinarily)</span></li>
  </ul>
</main>
</body>
</html>
```